Business Card Design

Stronger Care Network for the Riverlands is a partnership of twenty different health organisations in the western suburbs of Melbourne, working together to improve the health of the local community. The western suburbs of Melbourne is one of the fastest growing and most culturally diverse populations in Australia and its communities have some of the poorest health outcomes in Australia.
Please see location for copy of the SCNR:
http://qvlr.com.au/fileadmin/filemount/pdf_files/SCNFTR_13_FINAL_JUNE_2012.pdf
Updates

Reason: Hello. I've extended the deadline because in the brief I made a confusing mention about a logo, but I actually meant the 'Stronger Care Network for the Riverlands' jpg that I had already attached. Sorry about the confusion Thanks Rosalind

Hello, Thanks for the designs I have already received. I have extended the deadline because I made a confusing reference to a logo in my brief, but I was talking about the 'Stronger Care Network for the Riverlands' jpg I had already attached. There is no other logo for me to provide.

Thanks, Rosalind

Target Market(s)

Health and state/local government managers and CEOs

Industry/Entity Type

Health

Contact Information for Business Card

Rosalind Tiernan
Executive Officer
Stronger Care Network for the Riverlands
Ph: 0438 295 614
Rosalind.Tiernan@kp.org.au

Requirements
Must have
• logo and details as provided.
Would prefer matt finish
I can't see that logo has successfully attached so if it has not, please email or call me to follow up.

```html
<!DOCTYPE html>
<html lang="en">
<head>
<meta charset="utf-8">
<title>Rosalind Tiernan — Business Card</title>
<link rel="stylesheet" href="https://fonts.googleapis.com/css2?family=EB+Garamond:wght@400;500&display=swap">
<style>
  :root {
    --lime: #b6ff3e;
    --sky: #36adff;
    --pink: #ff1d67;
    --aqua: #66ffff;
    --slate: #88a2a3;
    --white: #ffffff;
    --ink: #111111;
  }
  * { box-sizing: border-box; margin: 0; padding: 0; }
  html, body { width: 1200px; height: 741px; overflow: hidden; background: var(--lime); }
  .card {
    position: relative;
    width: 1200px;
    height: 741px;
    background: var(--lime);
    font-family: "EB Garamond", Georgia, serif;
    font-variant-caps: small-caps;
  }
  .panel {
    position: absolute;
    left: 41px; top: 43px;
    width: 1015px; height: 654px;
    background: var(--sky);
  }
  .stripe { position: absolute; left: 1056px; width: 103px; }
  .stripe--pink { top: 43px; height: 219px; background: var(--pink); }
  .stripe--aqua { top: 262px; height: 216px; background: var(--aqua); }
  .stripe--slate { top: 478px; height: 219px; background: var(--slate); }

  .identity {
    position: absolute;
    left: 240px; top: 112px;
    width: 722px;
    text-align: center;
    color: var(--white);
  }
  .identity__name {
    display: inline-block;
    font-size: 56px;
    font-weight: 400;
    letter-spacing: 3px;
    line-height: 1;
    padding: 0 6px 8px;
    border-bottom: 4px solid var(--white);
  }
  .identity__role {
    font-size: 44px;
    letter-spacing: 3px;
    line-height: 1;
    margin-top: 8px;
  }

  .org {
    position: absolute;
    left: 103px; top: 296px;
    line-height: 1;
  }
  .org__main { color: var(--white); font-size: 46px; letter-spacing: 3px; }
  .org__link { color: var(--lime); font-size: 44px; letter-spacing: 3px; margin-top: 14px; }
  .org__place { color: var(--lime); font-size: 48px; letter-spacing: 3px; margin-top: 12px; }

  .contact {
    position: absolute;
    left: 103px;
    display: flex;
    align-items: center;
    color: var(--ink);
    font-size: 37px;
    letter-spacing: 3px;
    line-height: 1;
  }
  .contact svg { width: 46px; height: 46px; margin-right: 37px; flex: none; }
  .contact--phone { top: 520px; }
  .contact--email { top: 584px; }
</style>
</head>
<body>
  <div class="card">
    <div class="panel"></div>
    <div class="stripe stripe--pink"></div>
    <div class="stripe stripe--aqua"></div>
    <div class="stripe stripe--slate"></div>

    <div class="identity">
      <h1 class="identity__name">Rosalind Tiernan</h1>
      <p class="identity__role">Executive Officer</p>
    </div>

    <div class="org">
      <p class="org__main">Stronger Care Network</p>
      <p class="org__link">for the</p>
      <p class="org__place">Riverlands</p>
    </div>

    <p class="contact contact--phone">
      <svg viewBox="0 0 24 24" aria-hidden="true"><path fill="#111" d="M6.6 10.8a15.2 15.2 0 0 0 6.6 6.6l2.2-2.2a1 1 0 0 1 1-.25 11.4 11.4 0 0 0 3.6.57 1 1 0 0 1 1 1V20a1 1 0 0 1-1 1A17 17 0 0 1 3 4a1 1 0 0 1 1-1h3.5a1 1 0 0 1 1 1c0 1.25.2 2.45.57 3.6a1 1 0 0 1-.25 1z"/></svg>
      0438 295 614
    </p>
    <p class="contact contact--email">
      <svg viewBox="0 0 24 24" aria-hidden="true"><rect x="2" y="5" width="20" height="14" rx="1.5" fill="none" stroke="#111" stroke-width="2.4"/><path d="M3 6.5l9 7 9-7" fill="none" stroke="#111" stroke-width="2.4"/></svg>
      Rosalind.Tiernan@kp.org.au
    </p>
  </div>
</body>
</html>
```